Bright Ledger Works Double Sided DL Flyer

We need a double sided flyer that we provide to a Real Estate agent for leeds. It should provide our basic services as well as a modern look and feel. The brochure should incorporate our Brand colors and have a graphic that centres around money and property. I have included a couple of pictures that we like (but have not yet purchased from PIXVALE) as an indication of the type of picture we like.

WE need to also show the Bright Ledger Works brand and have our Phone / address's and email details.

Target Market(s)

Realestate clients (Property Investors)

Industry/Entity Type

Financial Planning

Requirements
Must have
• Picture on Front (maybe the logo on back)
• Please incorporate existing logo colours.

```html
<!DOCTYPE html>
<html lang="en">
<head>
<meta charset="utf-8">
<title>Bright Ledger Works DL Flyer</title>
<link rel="stylesheet" href="https://fonts.googleapis.com/css2?family=Ubuntu:wght@500;700&family=Oswald:wght@500;600&family=PT+Sans+Narrow:wght@700&family=Source+Sans+3:wght@300;400&display=swap">
<style>
:root{
  --page:#f1ede6;
  --green:#8cc63f;
  --green-dark:#5e9a2a;
  --green-deep:#3f7a1f;
  --orange:#f5a02a;
  --orange-soft:#eea05e;
  --red:#d9262e;
  --ink:#1a1a1a;
  --white:#ffffff;
}
*{margin:0;padding:0;box-sizing:border-box}
html,body{width:1200px;height:1152px;overflow:hidden;background:var(--page)}
.sheet{position:relative;width:1200px;height:1152px}
.panel{position:absolute;top:105px;width:471px;height:942px;overflow:hidden;box-shadow:4px 6px 10px rgba(0,0,0,.25)}
.panel--back{left:99px;background:radial-gradient(circle at 30% 45%,#a6d86a 0%,#7fc043 45%,#5fa832 100%)}
.panel--front{left:626px;background:var(--white)}
.wave{position:absolute;left:0;width:471px}
.services{position:absolute;left:55px;top:100px;width:400px;color:var(--white);font-family:Ubuntu,sans-serif}
.services__title{font-size:27px;font-weight:500;letter-spacing:.5px}
.services__lead{margin-top:8px;font-size:19px;font-weight:700;line-height:26px;color:#1c2b10}
.services__list{list-style:none;margin-top:14px}
.services__item{position:relative;padding-left:27px;font-size:18.5px;font-weight:500;line-height:24px;color:#1c2b10;margin-bottom:10px}
.services__item::before{content:"";position:absolute;left:0;top:4px;width:14px;height:14px;border-radius:50%;background:var(--white);border:1px solid #556}
.callout{position:absolute;left:29px;top:463px;width:410px;height:57px;border-radius:8px;background:var(--red);color:var(--white);font-family:"PT Sans Narrow",sans-serif;font-size:20px;line-height:25px;text-align:center;padding-top:4px}
.about{position:absolute;left:29px;top:545px;width:164px;font-family:"Source Sans 3",sans-serif;font-weight:400;font-size:13px;line-height:18px;color:#1c2b10;text-align:justify}
.about p+p{margin-top:9px}
.card{position:absolute;left:219px;top:547px;width:221px;height:363px;background:var(--white);border:2px solid var(--green-deep);text-align:center;font-family:"Source Sans 3",sans-serif}
.brand{font-family:Ubuntu,sans-serif;font-weight:700;color:var(--green-dark);display:flex;align-items:center;justify-content:center;gap:8px}
.brand__dot{border-radius:50%;background:var(--green-dark);flex:none}
.card .brand{margin-top:26px;font-size:17px}
.card .brand__dot{width:12px;height:12px}
.card__name{margin-top:30px;font-family:Oswald,sans-serif;font-weight:600;font-size:27px;color:var(--green-dark);line-height:32px}
.card__role{font-size:17px;font-weight:300;color:#333;margin-top:2px}
.card__call{margin:14px 10px 0;height:69px;background:var(--orange);color:var(--white);font-family:Oswald,sans-serif;font-weight:500;line-height:30px;padding-top:4px}
.card__call span{display:block;font-size:20px}
.card__call strong{display:block;font-size:28px;font-weight:600}
.card__address{margin-top:18px;font-size:16px;line-height:20px;color:var(--ink)}
.card__rule{margin:14px 14px 0;border-top:1px solid var(--green)}
.card__abn{margin-top:8px;font-size:16px;color:var(--ink)}
.photo{position:absolute;left:0;top:0;width:471px;height:366px;background:linear-gradient(180deg,#e9ecef 0%,#dfe4e3 45%,#c9d9b4 75%,#eef0ec 100%)}
.front-brand{position:absolute;left:0;top:392px;width:471px;font-size:30px}
.front-brand .brand__dot{width:22px;height:22px}
.pitch{position:absolute;left:0;top:560px;width:471px;text-align:center;color:var(--white)}
.pitch__title{font-family:Oswald,sans-serif;font-weight:600;font-size:44px;line-height:52px;text-shadow:1px 2px 2px rgba(0,0,0,.35)}
.pitch__sub{margin-top:14px;font-family:Ubuntu,sans-serif;font-weight:700;font-size:26px;line-height:34px}
.phone{position:absolute;left:0;top:765px;width:471px;display:flex;justify-content:center;align-items:center;gap:16px;font-family:Oswald,sans-serif;font-weight:600;font-size:42px;color:var(--ink)}
.front-rule{position:absolute;left:37px;top:829px;width:397px;border-top:1.5px solid #2a3a1a}
.contact{position:absolute;left:0;width:471px;text-align:center;font-family:Ubuntu,sans-serif;font-weight:700}
.contact--email{top:845px;font-size:19px;color:var(--white);letter-spacing:.5px}
.contact--web{top:876px;font-size:24px;color:var(--ink)}
</style>
</head>
<body>
<div class="sheet">

  <section class="panel panel--back">
    <svg class="wave" style="top:0;height:120px" viewBox="0 0 471 120" preserveAspectRatio="none">
      <path d="M0 0H471V55C350 70 240 40 140 45C80 48 30 70 0 100Z" fill="#ffffff"/>
      <path d="M0 45C60 25 140 30 220 38C320 48 400 55 471 50" fill="none" stroke="#d8d8d8" stroke-width="6"/>
      <path d="M0 110C40 80 90 55 160 48C260 40 360 60 471 68" fill="none" stroke="var(--orange-soft)" stroke-width="6"/>
    </svg>

    <div class="services">
      <h2 class="services__title">SERVICES</h2>
      <p class="services__lead">Accountants and Financial Advisors who specialise in:</p>
      <ul class="services__list">
        <li class="services__item">Negative Gearing &amp; Investment Properties</li>
        <li class="services__item">Property &amp; Capital Gains Tax Minimisation</li>
        <li class="services__item">Self-Managed Superannuation Funds (SMSF)</li>
        <li class="services__item">Small Business &amp; Personal Taxation</li>
        <li class="services__item">Investment Advice &amp; Risk Insurances</li>
      </ul>
    </div>

    <div class="callout">Contact us today and discover how we can help<br>you Build Your Business &amp; Grow Your Wealth.</div>

    <div class="about">
      <p>We specialise in helping ambitious business owners grow their business, their profits and their wealth.</p>
      <p>As a business advisory firm you'll find we do more than just 'keep the score' for our clients and it's our services beyond tax returns and financial statements that distinguish us from other local accounting firms. If you need assistance with your marketing including your branding, website, videos, digital publishing or social media strategies we have the skills and expertise to help you accelerate your business growth.</p>
    </div>

    <div class="card">
      <div class="brand"><span class="brand__dot"></span>Bright Ledger Works</div>
      <div class="card__name">Owen Hartley</div>
      <div class="card__role">Advisor / Accountant</div>
      <div class="card__call"><span>Call me:</span><strong>(02) 4000 1234</strong></div>
      <div class="card__address">Suite 8 / 41 Harbour View Road,<br>P O Box 2210,<br>Seacliff NSW 2261</div>
      <div class="card__rule"></div>
      <div class="card__abn">ABN 12 345 678 901</div>
    </div>
  </section>

  <section class="panel panel--front">
    <div class="photo" role="img" aria-label="Photo of cupped hands holding a small wooden house behind rising stacks of coins with green seedlings growing from them"></div>

    <div class="brand front-brand"><span class="brand__dot"></span>Bright Ledger Works</div>

    <svg class="wave" style="top:460px;height:482px" viewBox="0 0 471 482" preserveAspectRatio="none">
      <path d="M0 80C120 40 260 60 340 50C400 42 440 25 471 5V482H0Z" fill="var(--green)"/>
      <path d="M0 62C120 30 260 45 340 38C400 32 440 18 471 0" fill="none" stroke="#e6e3d0" stroke-width="10"/>
      <path d="M0 72C120 40 260 56 340 46C400 38 440 22 471 6" fill="none" stroke="var(--orange-soft)" stroke-width="7"/>
    </svg>

    <div class="pitch">
      <h1 class="pitch__title">Looking to GROW<br>Your Business?</h1>
      <p class="pitch__sub">We are a professional<br>accounting firm</p>
    </div>

    <div class="phone">
      <svg width="48" height="40" viewBox="0 0 48 40" aria-hidden="true">
        <path d="M4 14C4 6 44 6 44 14L38 18L32 13H16L10 18Z" fill="#3a7bd5"/>
        <path d="M12 20H36L42 36H6Z" fill="#e9ecef" stroke="#7a8590" stroke-width="1.5"/>
        <circle cx="24" cy="28" r="6" fill="#fff" stroke="#3a7bd5" stroke-width="2"/>
      </svg>
      <span>(02) 4000 1234</span>
    </div>
    <div class="front-rule"></div>
    <div class="contact contact--email">info@brightledgerworks.com.au</div>
    <div class="contact contact--web">www.brightledgerworks.com.au</div>
  </section>

</div>
</body>
</html>
```